New Coffee Brand Packaging Design

We need a package design for our new coffee brand called Brindle Oak Coffee. Our brand mission will be displayed on the packaging (along the side or the back) and we currently have a logo that should be displayed on the front. Feel free to suggest a new logo design as you are designing the packaging if it doesn't fit with your vision. The final design should be creative and conservative. We like coffee colors (dark and light browns, white, cream, black, gold). We also like chalkboard art imagery (i.e. coffee cups, theme words from our mission, people, etc.). One famous person from Lower Ashby Flats is Terrence Vogt (world famous boxer and activist). If there is a way to draw his image in more of an abstract way where it doesn't infringe any patents that would be the sort of creativity we would like in the packaging. Our coffee brand prides itself on being a coffee for the people. For the average joe, working American who enjoys a good cup of coffee and a good atmosphere.

Brindle Oak Coffee Mission: "We aim to be a coffee company for the people. The people who have an appreciation and love for family, community and who never forget where they came from. Our coffee was born out of Lower Ashby Flats…a place like many others where the hearts, the minds and the wills are strong. We hope you enjoy each and every cup. Peace & Blessings."

Requirements
Must have
• (On the side or on the back of the packaging) Brindle Oak Coffee Mission: "We aim to be a coffee company for the people. The people who have an appreciation and love for family, community and who never forget where they came from. Our coffee was born out of Lower Ashby Flats…a place like many others where the hearts, the minds and the wills are strong. We hope you enjoy each and every cup. Peace & Blessings."
Nice to have
• Coffee Colors: dark and light browns, white, cream, black, gold

```html
<!DOCTYPE html>
<html lang="en">
<head>
<meta charset="utf-8">
<title>Brindle Oak Coffee – Packaging Layout</title>
<link rel="stylesheet" href="https://fonts.googleapis.com/css2?family=Abel&family=Arimo:wght@700&family=Bebas+Neue&display=swap">
<style>
  :root {
    --canvas: #ffffff;
    --cream: #e8dac0;
    --ink: #231f1c;
    --black: #000000;
    --bean-dark: #1a140f;
    --bean-mid: #3b2c1f;
    --gold: #f5b324;
    --rule: #3a3430;
  }
  * { margin: 0; padding: 0; box-sizing: border-box; }
  html, body {
    width: 1200px; height: 1053px; overflow: hidden;
    background: var(--canvas);
  }
  .canvas { position: relative; width: 1200px; height: 1053px; }

  .panel-label {
    position: absolute; top: 117px; width: 200px; margin-left: -100px;
    text-align: center;
    font-family: "Arimo", Arial, sans-serif; font-weight: 700; font-size: 23px;
    color: var(--black);
  }

  .bag-art { position: absolute; left: 0; top: 0; width: 1200px; height: 1053px; }

  .panel-flat {
    position: absolute; top: 166px; width: 281px; height: 769px;
    background: var(--cream);
  }
  .panel-front { left: 45px; }
  .panel-back { left: 630px; }

  .brand-seal {
    position: absolute; border-radius: 50%; background: var(--black);
    display: flex; flex-direction: column; align-items: center; justify-content: center;
    font-family: "Abel", sans-serif; color: var(--gold); text-align: center; line-height: 1.05;
  }
  .brand-seal--front { left: 27px; top: 94px; width: 225px; height: 225px; font-size: 34px; }
  .brand-seal--side { width: 148px; height: 148px; top: 670px; font-size: 22px; }
  .brand-seal--side.left { left: 402px; }
  .brand-seal--side.right { left: 988px; }

  .front-info {
    position: absolute; left: 0; right: 0; top: 521px; text-align: center; color: var(--ink);
  }
  .front-info .grade { font-family: "Bebas Neue", sans-serif; font-size: 36px; letter-spacing: 1px; line-height: 1; color: #3c3632; }
  .front-info .blend { font-family: "Abel", sans-serif; font-size: 32px; line-height: 1.15; }
  .front-info .rule { width: 148px; height: 2px; background: var(--rule); margin: 14px auto 20px; }
  .front-info .weight { font-family: "Abel", sans-serif; font-size: 19px; }

  .mission {
    position: absolute; left: 0; right: 0; top: 42px; text-align: center;
    font-family: "Abel", sans-serif; font-size: 19px; line-height: 29.3px; color: var(--ink);
  }
  .mission b { font-family: "Bebas Neue", sans-serif; font-weight: 400; font-size: 22px; letter-spacing: 0.3px; }
  .mission .title { font-family: "Bebas Neue", sans-serif; font-size: 22px; letter-spacing: 0.5px; color: #3c3632; }
  .mission p { margin-bottom: 29px; }
  .mission .sign-off { font-family: "Bebas Neue", sans-serif; font-size: 22px; letter-spacing: 0.5px; margin-top: 29px; }

  .boxer-figure {
    display: block; width: 78px; height: 106px; margin: -8px auto 20px;
    border-radius: 10px;
    background: linear-gradient(180deg, #4a423c, #2c2622);
  }
</style>
</head>
<body>
<div class="canvas">
  <div class="panel-label" style="left:184px">Front</div>
  <div class="panel-label" style="left:478px">Side</div>
  <div class="panel-label" style="left:770px">Back</div>
  <div class="panel-label" style="left:1064px">Side</div>

  <svg class="bag-art" viewBox="0 0 1200 1053" xmlns="http://www.w3.org/2000/svg">
    <defs>
      <linearGradient id="bean-fill" x1="0" y1="0" x2="1" y2="1">
        <stop offset="0" stop-color="#1a140f"/>
        <stop offset="0.5" stop-color="#3b2c1f"/>
        <stop offset="1" stop-color="#1a140f"/>
      </linearGradient>
    </defs>
    <g role="img" aria-label="Side gusset with scattered roasted coffee bean pattern">
      <path fill="url(#bean-fill)" d="M471.1,246 V177 Q471.1,170 478.1,170 Q485.1,170 485.1,177 V246 L571.9,463 V923 Q571.9,935 559.9,935 H396.4 Q384.4,935 384.4,923 V463 Z"/>
      <path fill="#000000" d="M471.1,250 V177 Q471.1,170 478.1,170 Q485.1,170 485.1,177 V250 Z"/>
    </g>
    <g role="img" aria-label="Side gusset with scattered roasted coffee bean pattern" transform="translate(586 0)">
      <path fill="url(#bean-fill)" d="M471.1,246 V177 Q471.1,170 478.1,170 Q485.1,170 485.1,177 V246 L571.9,463 V923 Q571.9,935 559.9,935 H396.4 Q384.4,935 384.4,923 V463 Z"/>
      <path fill="#000000" d="M471.1,250 V177 Q471.1,170 478.1,170 Q485.1,170 485.1,177 V250 Z"/>
    </g>
  </svg>

  <div class="brand-seal brand-seal--side left">Brindle Oak<br>Coffee</div>
  <div class="brand-seal brand-seal--side right">Brindle Oak<br>Coffee</div>

  <section class="panel-flat panel-front">
    <div class="brand-seal brand-seal--front">Brindle Oak<br>Coffee</div>
    <div class="front-info">
      <div class="grade">Premium</div>
      <div class="blend">Blend</div>
      <div class="rule"></div>
      <div class="weight">120 grams / 8.8 oz.</div>
    </div>
  </section>

  <section class="panel-flat panel-back">
    <div class="mission">
      <p class="title">Brindle Oak Coffee<br>Mission:</p>
      <p><b>WE</b> aim to be a <b>COFFEE</b><br><b>COMPANY</b> for the <b>PEOPLE</b>.<br>The <b>PEOPLE</b> who have an<br><b>APPRECIATION</b> and <b>LOVE</b> for<br><b>FAMILY, COMMUNITY</b> and who<br><b>NEVER FORGET</b> where they<br>came <b>FROM</b>.</p>
      <span class="boxer-figure" role="img" aria-label="Silhouette of a boxer in fighting stance"></span>
      <div>Our coffee was born out<br>of <b>LOWER ASHBY FLATS</b><br>...a place like many others<br>where the <b>HEARTS</b>, the <b>MINDS</b><br>and the <b>WILLS</b> are <b>STRONG</b>.<br>We hope you <b>ENJOY</b><br>each and every cup.</div>
      <div class="sign-off">Peace &amp; Blessings.</div>
    </div>
  </section>
</div>
</body>
</html>
```